Biz technology consulting firm like a global company (better than Corvantis, etc)

Check word document high level requirements, a_design_webpage_content attached providing more details for content and message to convey to potential customers..  Create a crisp, clear and engaging business consulting website design that allows the user to understand the value that Brimquarta can deliver to their company.  We focus on innovation, simplification, creative solutions, digital transformations ERP, CRM, Analytics, project management, making IT simple and coaching enterprises how to align and implement technologies to support business strategy and goals. Whether a startup or a global billion dollar firm, we increase EBITDA through innovation and digital transformation.  

I desire to have sections that highlight each of the core areas such as: (**Please see  brimquarta.example and the design word document that is attached below for core areas of focus**)

Feel free to go to Brimquarta.example and review the basic categories to understand at a very high level the categories that are key.

Help me create a brand and website that engages startups, Private Equity firms seeking carve-out, integration experience and large corporate enterprises searching to convert to data driven and customer focused enterprises.  
Hero section with a tagline that emphasizes the company's focus on Walking UP bolder.  We help you visualize outcomes with a positive and collaborative solution driven mindset.  When you look at life through a different "positive" lens, you can convert all problems to opportunities.  Align your IT team with your business goals and you quickly realize the value of all processes and technology deployed in your enterprise; increasing EBITDA, morale, and long term success.

We evaluate your current state, create a custom roadmap for alignment, coach  and empower you to lead while removing the uncertainty and silos.  Partner with the experts who help make business and technology simple and effective
Call-to-action section encouraging visitors to learn more about the company's services and expertise
Services -- detail provided in the attached word document (please use)
Section providing an overview of the company's services, including digital transformation, strategy, change management, CRM, ERP, automation, AI, data / analytics, process optimization, carve-outs, integrations, scaling, risk mitigation, security and marketing.
Call-to-action section encouraging visitors to learn more about the company's expertise and how it can help their business and encouraging visitors to schedule a consultation or assessment.
Footer
Navigation menu
Contact information
LinkedIn link
The website should have a modern and professional design, with a focus on clear messaging and easy navigation. The color scheme will be clean and simple, with a mix of colors to convey trust, reliability, and innovation. The website will be optimized for search engines and mobile devices, ensuring that visitors can easily access the site from any device.

Target Market(s)

Companies who desire to grow their business, optimize their processes, maximize the output of human capital and profitablity.

Industry/Entity Type

Business Technology consulting

Coding

Coded - Design and coding required

Number of Pages Required

4 page

Font styles to use
Other font styles liked:
• designer should choose for professional audience

Requirements
Must have
• easy navigation, engaging flow, professional layout and colors that represent confidence, excellence and innovation in a world full of change.
Nice to have
• I would like to see you blend in the play on DELTA's (changes that we face in business and life), the different way we may look at things and the unique way we solve problems. All of these are options to Walk UP bolder and leverage the unique views of individuals, millions of data points, workflow and technology enablers to deliver maximize value to your enterprise

```html
<!DOCTYPE html>
<html lang="en">
<head>
<meta charset="UTF-8">
<title>Brimquarta – Business Technology Consulting</title>
<link href="https://fonts.googleapis.com/css2?family=Arimo:wght@400;700&family=Tinos:wght@400;700&display=swap" rel="stylesheet">
<style>
:root{
  --brand:#2a4f8f;
  --brand-dark:#1a2d52;
  --navy:#141a45;
  --navy-2:#0a2450;
  --ink:#111111;
  --page:#f5f7fc;
  --stripe:#ffffff;
  --soft-blue:#c5d5ea;
  --pale-blue:#e3e9f5;
  --link-blue:#2a5aa8;
  --white:#ffffff;
}
*{margin:0;padding:0;box-sizing:border-box}
html,body{width:1200px;height:3905px;overflow:hidden}
body{font-family:"Arimo",Arial,sans-serif;color:var(--ink);background:var(--page)}
.page{position:relative;width:1200px;height:3905px;overflow:hidden}
.abs{position:absolute}

/* header */
.site-header{position:absolute;left:0;top:0;width:1200px;height:86px;background:var(--white)}
.brand{position:absolute;left:100px;top:29px;display:flex;align-items:center;gap:8px;color:var(--brand);font-weight:700;font-size:22px}
.brand .mark{width:24px;height:24px;border:2px solid var(--brand);border-radius:3px}
.main-nav{position:absolute;top:34px;left:450px;display:flex;gap:0;font-size:15px}
.main-nav a{position:absolute;color:var(--ink);text-decoration:none;white-space:nowrap}
.btn{display:flex;align-items:center;justify-content:center;border-radius:30px;text-decoration:none;font-size:16px}
.btn-primary{background:var(--brand);color:var(--white)}
.btn-light{background:var(--white);color:var(--brand)}
.header-cta{position:absolute;left:930px;top:19px;width:168px;height:49px}

/* hero */
.hero{position:absolute;left:0;top:86px;width:1200px;height:635px;background:linear-gradient(160deg,#1c2a5c 0%,#173f72 45%,#162058 75%,#1a1745 100%)}
.hero-art{position:absolute;inset:0;background:radial-gradient(circle at 80% 70%,rgba(60,140,190,.35),transparent 45%),radial-gradient(circle at 15% 50%,rgba(60,130,180,.3),transparent 40%)}
.hero h1{position:absolute;left:0;width:1200px;top:78px;text-align:center;color:var(--white);font-weight:400;font-size:79px;line-height:90px;letter-spacing:-.5px}
.hero p{position:absolute;left:350px;width:500px;top:295px;text-align:center;color:var(--white);font-size:16px;line-height:19px}
.hero .btn{position:absolute;left:506px;top:388px;width:187px;height:49px}

/* about */
.about{position:absolute;left:0;top:721px;width:1200px;height:833px;background:var(--page)}
.stripe{position:absolute;top:0;bottom:0;width:71px;background:var(--stripe)}
.about .blob{position:absolute;left:0;top:109px;width:435px;height:641px;background:var(--soft-blue);border-radius:0 90px 90px 0}
.about .photo{position:absolute;left:106px;top:170px;width:494px;height:519px;border-radius:14px;background:radial-gradient(circle at 50% 35%,#3a7fc8 0%,#133058 35%,#0a1426 70%),#0a1426}
.about h2{position:absolute;left:680px;top:192px;font-weight:400;font-size:33px}
.about .copy{position:absolute;left:680px;top:294px;width:420px;font-size:15px;line-height:19px}
.about .copy p{margin-bottom:19px}
.about .copy .lead{margin-bottom:38px}
.about .btn{position:absolute;left:680px;top:620px;width:187px;height:48px}

/* services */
.services{position:absolute;left:0;top:1554px;width:1200px;height:947px;background:linear-gradient(180deg,#062c55 0%,#07224e 50%,#0a1745 100%)}
.services-art{position:absolute;inset:0;background:radial-gradient(ellipse at 50% 45%,rgba(40,150,200,.35),transparent 55%)}
.services h2{position:absolute;left:0;width:1200px;top:60px;text-align:center;color:var(--white);font-weight:400;font-size:33px}
.services .intro{position:absolute;left:350px;width:500px;top:121px;text-align:center;color:var(--white);font-size:16px;line-height:19px}
.service-panel{position:absolute;left:100px;top:228px;width:1000px;height:612px;border-radius:8px;background:rgba(70,90,140,.45)}
.service-card{position:absolute;left:365px;top:0;width:270px;height:274px;border-radius:8px;background:rgba(255,255,255,.3)}
.service{position:absolute;width:220px;text-align:center;color:var(--white);font-size:16px;line-height:19px}
.service svg{display:block;margin:0 auto 12px}

/* contact */
.contact{position:absolute;left:0;top:2501px;width:1200px;height:696px;background:var(--page)}
.contact .back{position:absolute;left:547px;top:99px;width:603px;height:515px;background:var(--pale-blue)}
.call{position:absolute;left:79px;top:365px;color:var(--link-blue);font-size:16px}
.call .phone{margin-top:20px}
.call .note{margin-top:68px;width:330px;line-height:20px}
.message-form{position:absolute;left:483px;top:2657px;width:632px;height:622px;background:linear-gradient(180deg,#2a4f8f 0%,#1a2d52 100%);z-index:3}
.message-form h2{position:absolute;left:0;width:632px;top:88px;text-align:center;color:var(--white);font-weight:400;font-size:36px}
.field{position:absolute;left:94px;width:437px;height:52px;border-bottom:1px solid rgba(255,255,255,.8);font-family:"Tinos","Times New Roman",serif;color:var(--white);font-size:17px}
.send{position:absolute;left:347px;top:488px;width:184px;height:49px;background:var(--white);color:var(--brand-dark);font-family:"Tinos","Times New Roman",serif;font-size:17px;display:flex;align-items:center;justify-content:center}

/* footer */
.site-footer{position:absolute;left:0;top:3197px;width:1200px;height:708px;background:linear-gradient(135deg,#0b1d33 0%,#0f3a4a 40%,#0a1a30 70%,#050b16 100%)}
.footer-art{position:absolute;inset:0;background:radial-gradient(circle at 70% 25%,rgba(40,190,200,.25),transparent 35%)}
.footer-brand{position:absolute;left:115px;top:324px;display:flex;align-items:center;gap:14px;color:var(--white);font-weight:700;font-size:46px}
.footer-brand .mark{width:58px;height:46px;border:3px solid var(--white);border-radius:4px}
.footer-about{position:absolute;left:115px;top:431px;width:330px;color:var(--white);font-size:16px;line-height:20px}
.footer-col{position:absolute;top:320px;color:var(--white);font-size:14px}
.footer-col h3{font-weight:400;font-size:18px;margin-bottom:14px}
.footer-col li{list-style:none;margin-bottom:17px}
.social{position:absolute;left:839px;top:322px;color:var(--white)}
.social h3{font-weight:400;font-size:20px;margin-bottom:12px}
.social .dots{display:flex;gap:8px}
.social .dots span{width:30px;height:30px;border-radius:50%;border:1.5px solid var(--white);background:rgba(255,255,255,.25);display:flex;align-items:center;justify-content:center}
.legal{position:absolute;top:646px;left:0;width:1200px;color:var(--white);font-size:15px}
.legal .copy{position:absolute;left:180px}
.legal a{color:var(--white)}
.legal .code{position:absolute;left:1069px}
</style>
</head>
<body>
<div class="page">

<header class="site-header">
  <div class="brand"><span class="mark"></span>brimquarta</div>
  <nav class="main-nav">
    <a href="#" style="left:0">Home</a>
    <a href="#" style="left:68px">About</a>
    <a href="#" style="left:136px">Services</a>
    <a href="#" style="left:221px">Contact</a>
  </nav>
  <a href="#" class="btn btn-primary header-cta">Get Started</a>
</header>

<section class="hero">
  <div class="hero-art" role="img" aria-label="Blue technology circuitry and gears backdrop"></div>
  <h1>Welcome to Brimquarta<br>Walk UP bolder</h1>
  <p>Lorem Ipsum is simply dummy text of the printing Lorem Ipsum is simply dummy text of the printing</p>
  <a href="#" class="btn btn-light">Learn More</a>
</section>

<section class="about">
  <div class="stripe" style="left:182px"></div>
  <div class="stripe" style="left:435px"></div>
  <div class="stripe" style="left:686px"></div>
  <div class="stripe" style="left:939px"></div>
  <div class="blob"></div>
  <div class="photo" role="img" aria-label="Hand holding a glowing digital building model above a laptop keyboard"></div>
  <h2>About Us</h2>
  <div class="copy">
    <p class="lead">Welcome to Brimquarta</p>
    <p>Transforming the Way You Do Business<br>Every business is unique. That's why we take a personalized approach to every project, working closely with you to understand your goals and create tailored solutions that work for you.</p>
    <p>Transforming the Way You Do Business<br>Every business is unique. That's why we take a personalized approach to every project, working closely with you to understand your goals and create tailored solutions that work for you.</p>
  </div>
  <a href="#" class="btn btn-primary">Learn More</a>
</section>

<section class="services">
  <div class="services-art" role="img" aria-label="Glowing world map with orbiting network lines"></div>
  <h2>Services</h2>
  <p class="intro">Lorem Ipsum is simply dummy text of the printing Lorem Ipsum is simply dummy text of the printing</p>
  <div class="service-panel">
    <div class="service-card"></div>

    <div class="service" style="left:60px;top:138px">
      <svg width="86" height="86" viewBox="0 0 86 86" fill="none" stroke="#fff" stroke-width="3">
        <path d="M22 52a14 14 0 0 1 2-28 20 20 0 0 1 38 4 12 12 0 0 1 0 24z"/>
        <rect x="26" y="32" width="34" height="14" rx="5"/>
        <path d="M33 52v14M43 52v20M53 52v14"/><circle cx="33" cy="70" r="3"/><circle cx="43" cy="76" r="3"/><circle cx="53" cy="70" r="3"/>
      </svg>
      Saas CRM
    </div>

    <div class="service" style="left:390px;top:70px">
      <svg width="86" height="86" viewBox="0 0 86 86" fill="none" stroke="#fff" stroke-width="3">
        <path d="M14 43a29 29 0 0 1 50-20M72 43a29 29 0 0 1-50 20"/>
        <path d="M64 12v11H53M22 74V63h11"/>
        <circle cx="43" cy="43" r="14"/><circle cx="43" cy="43" r="6"/>
        <path d="M43 25v5M43 56v5M25 43h5M56 43h5"/>
      </svg>
      Change Management
    </div>

    <div class="service" style="left:704px;top:135px">
      <svg width="86" height="86" viewBox="0 0 86 86" fill="none" stroke="#fff" stroke-width="3">
        <circle cx="38" cy="30" r="22"/><circle cx="38" cy="30" r="13"/><circle cx="38" cy="30" r="4"/>
        <path d="M38 30v30a6 6 0 0 0 12 0V44a5 5 0 0 1 10 0v22M26 52v10a14 14 0 0 0 10 12"/>
      </svg>
      Digital<br>Transformation
    </div>

    <div class="service" style="left:240px;top:392px">
      <svg width="86" height="86" viewBox="0 0 86 86" fill="none" stroke="#fff" stroke-width="3">
        <circle cx="40" cy="42" r="26"/><circle cx="40" cy="42" r="17"/>
        <path d="M40 14V8M40 76v-6M12 42H6M74 42h-6M20 22l-4-4M64 18l-4 4M20 62l-4 4"/>
        <path d="M40 42l8-6"/>
        <circle cx="64" cy="64" r="11"/><path d="M58 64l4 4 8-8"/>
      </svg>
      Procces<br>Optimization
    </div>

    <div class="service" style="left:546px;top:392px">
      <svg width="86" height="86" viewBox="0 0 86 86" fill="none" stroke="#fff" stroke-width="3">
        <path d="M40 12a30 30 0 0 0 0 62"/><path d="M40 24a18 18 0 0 0 0 38"/>
        <path d="M40 12v62M40 30h18M40 43h26M40 56h18M58 30l6-8M58 56l6 8"/>
        <circle cx="67" cy="19" r="4"/><circle cx="70" cy="43" r="4"/><circle cx="67" cy="67" r="4"/>
      </svg>
      Analyticals
    </div>
  </div>
</section>

<section class="contact">
  <div class="stripe" style="left:182px"></div>
  <div class="stripe" style="left:435px"></div>
  <div class="back"></div>
  <div class="call">
    <div>Call Us Today</div>
    <div class="phone">+1 555 014 72290</div>
    <p class="note">Lorem Ipsum is simply dummy text of the printing and typesetting industry. Lorem Ipsum is simply dummy text of the printing and typesetting industry.</p>
  </div>
</section>

<form class="message-form">
  <h2>Message Us</h2>
  <div class="field" style="top:170px">Name</div>
  <div class="field" style="top:277px">Email</div>
  <div class="field" style="top:373px">Tlpn</div>
  <div class="send">Sen Message</div>
</form>

<footer class="site-footer">
  <div class="footer-art" role="img" aria-label="Dark teal microchip grid with glowing data lights"></div>
  <div class="footer-brand"><span class="mark"></span>brimquarta</div>
  <p class="footer-about">Lorem Ipsum is simply dummy text of the printing and typesetting industry. Lorem Ipsum is simply dummy text of the printing and typesetting industry.</p>
  <div class="footer-col" style="left:520px">
    <h3>About</h3>
    <ul><li>About Us</li><li>Services</li><li>Contact</li></ul>
  </div>
  <div class="footer-col" style="left:667px">
    <h3>Contact</h3>
    <ul><li>+1 555 014 72290</li><li>hello@brimquarta.example</li></ul>
  </div>
  <div class="social">
    <h3>Socila Media</h3>
    <div class="dots">
      <span></span><span></span><span></span>
      <span><svg width="16" height="12" viewBox="0 0 16 12" fill="none" stroke="#fff" stroke-width="1.5"><rect x="1" y="1" width="14" height="10" rx="1"/><path d="M1 1l7 6 7-6"/></svg></span>
    </div>
  </div>
  <div class="legal">
    <span class="copy">Copyright © 2023 Halvernook Advisory Pty Ltd. All rights reserved.<a href="#">Privacy</a> | <a href="#">Terms of Use</a> | <a href="#">Sitemap</a></span>
    <span class="code">RO01</span>
  </div>
</footer>

</div>
</body>
</html>
```